Pest Control Company needs business card!

Hi there, we need a business card designed for our new Pest Control Company. Ideally this card will be simple, yet feel elegant and high end. We want to use the colours Orange, Black and White. Please see our attached logo for the exact colours.

Business card details:

Phone - 0461 275 804
Name - Gavin Holloway
Email - Info@steadfastverminguard.com.au

We would also like to include the following list with dot points:

SERVICES / INSPECTIONS

Termites, Wood Borers, Ants, Cockroaches, Spiders, Fleas, Mice, Rats, Bed Bugs, & More!

```html
<!DOCTYPE html>
<html lang="en">
<head>
<meta charset="UTF-8">
<title>Steadfast Vermin Guard – Business Cards</title>
<link rel="stylesheet" href="https://fonts.googleapis.com/css2?family=Roboto:wght@400;500;700;900&display=swap">
<style>
  :root {
    --backdrop: #ececec;
    --card-white: #ffffff;
    --card-yellow: #fddf1a;
    --ink: #1a1a1a;
    --ink-soft: #333333;
    --accent-red: #e0262b;
  }
  * { box-sizing: border-box; margin: 0; padding: 0; }
  html, body {
    width: 1200px;
    height: 800px;
    overflow: hidden;
    background: var(--backdrop);
    font-family: "Roboto", Arial, sans-serif;
    color: var(--ink);
  }
  .canvas { position: relative; width: 1200px; height: 800px; }

  .card {
    position: absolute;
    width: 571px;
    height: 331px;
    box-shadow: 0 6px 18px rgba(0,0,0,0.12);
  }

  /* Front: contact side */
  .card-contact { left: 475px; top: 31px; background: var(--card-white); }
  .card-contact .brand {
    position: absolute;
    right: 52px;
    top: 58px;
  }
  .contact-name {
    position: absolute;
    left: 48px;
    top: 160px;
    font-size: 21px;
    font-weight: 700;
    letter-spacing: 0.3px;
    text-transform: uppercase;
  }
  .name-rule {
    position: absolute;
    left: 48px;
    top: 194px;
    width: 16px;
    height: 2px;
    background: var(--ink);
  }
  .contact-list {
    position: absolute;
    left: 48px;
    top: 208px;
    list-style: none;
  }
  .contact-item {
    display: flex;
    align-items: center;
    gap: 8px;
    height: 25px;
    font-size: 19px;
    color: var(--ink-soft);
  }
  .contact-icon { width: 16px; height: 16px; flex: none; }

  /* Back: services side */
  .card-services { left: 169px; top: 406px; background: var(--card-yellow); }
  .card-services .brand {
    position: absolute;
    left: 50%;
    top: 70px;
    transform: translateX(-50%);
  }
  .service-list {
    position: absolute;
    left: 0;
    right: 0;
    top: 245px;
    text-align: center;
    font-size: 20px;
    line-height: 26px;
    color: var(--ink);
  }
  .service-list span::before { content: "\25CF\00A0"; font-size: 15px; vertical-align: 2px; }

  /* Company name block */
  .brand { display: flex; align-items: center; gap: 12px; }
  .brand-name {
    font-weight: 900;
    text-transform: uppercase;
    color: var(--ink);
    line-height: 0.95;
  }
  .card-contact .brand-name { font-size: 24px; }
  .card-services .brand-name { font-size: 34px; }
  .brand-dot { border-radius: 50%; background: var(--ink); flex: none; }
  .card-contact .brand-dot { width: 34px; height: 34px; }
  .card-services .brand-dot { width: 52px; height: 52px; }
</style>
</head>
<body>
<main class="canvas">

  <section class="card card-contact" aria-label="Business card contact side">
    <div class="brand">
      <div class="brand-name">Steadfast<br>Vermin<br>Guard</div>
      <span class="brand-dot" aria-hidden="true"></span>
    </div>

    <h1 class="contact-name">Gavin Holloway</h1>
    <div class="name-rule"></div>

    <ul class="contact-list">
      <li class="contact-item">
        <svg class="contact-icon" viewBox="0 0 16 16" aria-hidden="true">
          <path fill="#e0262b" d="M2 6c0-2 2.5-3 6-3s6 1 6 3v1h-3V5.5H5V7H2zM4 8h8l1.5 5h-11z"/>
          <circle cx="8" cy="10.5" r="1.6" fill="#fff"/>
        </svg>
        0461 275 804
      </li>
      <li class="contact-item">
        <svg class="contact-icon" viewBox="0 0 16 16" aria-hidden="true">
          <rect x="1.5" y="4" width="13" height="9" rx="1" fill="#e0262b"/>
          <path d="M1.5 4.5 8 9l6.5-4.5" fill="none" stroke="#fff" stroke-width="1.3"/>
        </svg>
        Info@steadfastverminguard.com.au
      </li>
      <li class="contact-item">
        <svg class="contact-icon" viewBox="0 0 16 16" aria-hidden="true">
          <circle cx="8" cy="8" r="6.3" fill="none" stroke="#e0262b" stroke-width="1.5"/>
          <ellipse cx="8" cy="8" rx="2.6" ry="6.3" fill="none" stroke="#e0262b" stroke-width="1.2"/>
          <path d="M2 8h12" stroke="#e0262b" stroke-width="1.2"/>
        </svg>
        www.steadfastverminguard.com.au
      </li>
    </ul>
  </section>

  <section class="card card-services" aria-label="Business card services side">
    <div class="brand">
      <div class="brand-name">Steadfast<br>Vermin<br>Guard</div>
      <span class="brand-dot" aria-hidden="true"></span>
    </div>

    <p class="service-list">
      <span>Termites</span> <span>Wood Borers</span> <span>Ants</span> <span>Cockroaches</span><br>
      <span>Spiders</span> <span>Fleas</span> <span>Mice</span> <span>Rats</span> <span>Bed Bugs, &amp; More!</span>
    </p>
  </section>

</main>
</body>
</html>
```